New Stationery New Logo for KT Mouldings Limited

We have a new logo and now want new stationary to go with it

This will be

Letterhead
Compliments Slip
Business Cards

Company details are
KT Mouldings Limited
Brindle Row, Rugby, Warwickshire, CV34 7HX, UK
Telephone : +44(0)1788 930467
Fax: +44(0)1788 918723
Email: sales@ktmouldings.example
Web: www.ktmouldings.example

Target Market(s)

Engineering / Metal Stamping

Industry/Entity Type

Manufacture

Contact Information for Business Card

Neil Garbutt
Business Development Manager
KT Mouldings Limited
Brindle Row
Rugby
Warwickshire
CV34 7HX, UK

T: +44(0)1788 930467
F: +44(0)1788 918723
E: sales@ktmouldings.example
W: www.ktmouldings.example

Font styles to use
Sans Serif

Colors
33a6d7
0555a3
3176b5
85cae6
85acd3

Requirements
Must have
• Logo

```html
<!DOCTYPE html>
<html lang="en">
<head>
<meta charset="utf-8">
<title>KT Mouldings – Business Cards</title>
<link rel="stylesheet" href="https://fonts.googleapis.com/css2?family=Montserrat:wght@400;500;700&display=swap">
<style>
  :root {
    --backdrop: #1c1c1e;
    --card-white: #f6f6f6;
    --card-dark: #2e2e30;
    --brand-blue: #0a3b8c;
    --ink: #2a2a2a;
    --band-grey: #3a3b3e;
    --light-text: #e8e8e8;
  }
  * { box-sizing: border-box; margin: 0; padding: 0; }
  html, body {
    width: 1200px; height: 1001px; overflow: hidden;
    background: var(--backdrop);
    font-family: "Montserrat", sans-serif;
  }
  .card {
    position: absolute; left: 306px; width: 588px; height: 330px;
    box-shadow: 0 4px 10px rgba(0,0,0,.5);
    overflow: hidden;
  }
  .card--front { top: 133px; background: var(--card-white); color: var(--ink); }
  .card--back { top: 539px; background: linear-gradient(160deg, #353537, var(--card-dark) 60%, #262628); }

  .holder { position: absolute; left: 40px; top: 114px; }
  .holder__name { color: var(--brand-blue); font-weight: 700; font-size: 18px; letter-spacing: .2px; }
  .holder__role { font-size: 14px; margin-top: 1px; }

  .contacts { position: absolute; left: 36px; top: 204px; list-style: none; font-size: 13.5px; }
  .contacts li { display: flex; align-items: center; height: 18.5px; }
  .contacts svg { width: 14px; height: 14px; margin-right: 9px; flex: none; }

  .address { position: absolute; right: 34px; top: 240px; text-align: right; font-size: 13.5px; line-height: 18.5px; }

  .brand { position: absolute; display: flex; align-items: center; font-weight: 500; letter-spacing: 7px; white-space: nowrap; }
  .brand__dot { border-radius: 50%; margin-right: 10px; flex: none; }
  .card--front .brand { right: 26px; top: 124px; font-size: 22px; color: var(--brand-blue); }
  .card--front .brand__dot { width: 14px; height: 14px; background: var(--brand-blue); }
  .card--back .brand { left: 0; right: 0; justify-content: center; top: 124px; font-size: 30px; color: var(--light-text); }
  .card--back .brand__dot { width: 18px; height: 18px; background: var(--brand-blue); }

  .band { position: absolute; left: 0; bottom: 0; width: 588px; height: 34px; }

  .web { position: absolute; left: 0; right: 0; top: 258px; text-align: center; font-size: 14px; color: var(--light-text); }
  .web strong { font-weight: 700; }
</style>
</head>
<body>

<section class="card card--front">
  <div class="holder">
    <p class="holder__name">ROWAN PELL</p>
    <p class="holder__role">General Manager</p>
  </div>

  <div class="brand"><span class="brand__dot"></span>KT MOULDINGS</div>

  <ul class="contacts">
    <li>
      <svg viewBox="0 0 14 14" aria-hidden="true"><rect width="14" height="14" rx="2" fill="#0a3b8c"/><path d="M4 3.2h2l.6 2-1 .8c.5 1.2 1.3 2 2.4 2.5l.8-1 2 .6v2c-4 .3-7-2.8-6.8-6.9z" fill="#fff"/></svg>
      +44(0)1788 930467
    </li>
    <li>
      <svg viewBox="0 0 14 14" aria-hidden="true"><rect width="14" height="14" rx="2" fill="#0a3b8c"/><rect x="4.5" y="2.5" width="5" height="3" fill="#fff"/><rect x="2.5" y="5.5" width="9" height="4" rx="1" fill="#fff"/><rect x="4.5" y="8.5" width="5" height="3" fill="#fff" stroke="#0a3b8c" stroke-width=".6"/></svg>
      +44(0)1788 918723
    </li>
    <li>
      <svg viewBox="0 0 14 14" aria-hidden="true"><rect width="14" height="14" rx="2" fill="#0a3b8c"/><rect x="2.5" y="4" width="9" height="6" fill="#fff"/><path d="M2.5 4l4.5 3.5L11.5 4" fill="none" stroke="#0a3b8c" stroke-width=".9"/></svg>
      sales@ktmouldings.example
    </li>
    <li>
      <svg viewBox="0 0 14 14" aria-hidden="true"><rect width="14" height="14" rx="2" fill="#0a3b8c"/><g fill="none" stroke="#fff" stroke-width=".9"><circle cx="7" cy="7" r="4.5"/><ellipse cx="7" cy="7" rx="2" ry="4.5"/><path d="M2.5 7h9M3.3 4.6h7.4M3.3 9.4h7.4"/></g></svg>
      www.ktmouldings.example
    </li>
  </ul>

  <address class="address" style="font-style:normal">
    Brindle Row, Rugby<br>
    Warwickshire, CV34 7HX, UK
  </address>

  <svg class="band" viewBox="0 0 588 34" aria-hidden="true">
    <polygon points="0,4 266,4 254,20 0,20" fill="var(--band-grey)"/>
    <polygon points="0,22 252,22 250,24 0,24" fill="#fff"/>
    <polygon points="0,26 250,26 246,34 0,34" fill="var(--brand-blue)"/>
    <polygon points="274,0 588,0 588,34 250,34 264,16 270,4" fill="var(--brand-blue)"/>
  </svg>
</section>

<section class="card card--back">
  <div class="brand"><span class="brand__dot"></span>KT MOULDINGS</div>
  <p class="web">www.<strong>ktmouldings</strong>.example</p>
</section>

</body>
</html>
```